Business Card for Orvane Parts Wholesale supplier

Hi There! I need a new business card for our company. We are specialized in selling Orvane parts, mostly we sell new LCD screens for Telvox and Slatrons. I would like to see that back in the design.

You can find the colors and logo's on our website: www.dorvak-example.nl

Industry/Entity Type

Business

Contact Information for Business Card

My Details:
Lars Vintorp

Phone: 0031612873406
E-mail: Lars@dorvak-example.nl

Slogan: "Because Quality Matters"

Font styles to use
Sans Serif

Colors

Designer to choose colors to be used in the design.

Requirements
Must have
• A Black backside with the Dorvak logo on it. The front side should be clean with only my contact details.
• But I'm also open for something really different or awesome!
Nice to have
• Remember that we are in the parts & repairing industry, So i'll be handing those business cards mainly to repair companies. Maybe you can do something with that thought :)

```html
<!DOCTYPE html>
<html lang="en">
<head>
<meta charset="utf-8">
<title>Dorvak Business Card</title>
<link href="https://fonts.googleapis.com/css2?family=Roboto:wght@400;500;700&display=swap" rel="stylesheet">
<style>
  :root {
    --page: #e6e6e6;
    --black: #141414;
    --panel: #1b1b1c;
    --orange: #f07220;
    --white: #ffffff;
    --paper: #f4f4f4;
    --grey-band: #9c9c9e;
    --ink: #1e1e1e;
    --ink-soft: #333333;
  }
  * { box-sizing: border-box; margin: 0; padding: 0; }
  html, body {
    width: 1200px; height: 576px; overflow: hidden;
    background: var(--page);
    font-family: "Roboto", Arial, sans-serif;
  }
  .canvas { position: relative; width: 1200px; height: 576px; }

  .card {
    position: absolute; top: 138px;
    width: 484px; height: 294px;
    border-radius: 14px; overflow: hidden;
  }

  /* Back side */
  .card-back { left: 82px; background: var(--black); }
  .card-back .photo-area {
    position: absolute; inset: 0;
    background:
      radial-gradient(ellipse 70% 50% at 60% 25%, #2e2e2f 0%, rgba(30,30,30,0) 70%),
      linear-gradient(160deg, #232324 0%, #1a1a1a 55%, #262627 100%);
  }
  .card-back .brand {
    position: absolute; left: 0; right: 0; top: 110px;
    display: flex; align-items: center; justify-content: center; gap: 14px;
  }
  .brand-dot { width: 46px; height: 46px; border-radius: 50%; background: var(--orange); }
  .brand-name {
    font-weight: 500; font-size: 58px; line-height: 1;
    color: var(--white); letter-spacing: 1px;
  }

  /* Front side */
  .card-front { left: 602px; width: 482px; height: 292px; }
  .card-front svg.layout { position: absolute; inset: 0; }
  .front-brand {
    position: absolute; left: 0; width: 246px; top: 74px;
    display: flex; flex-direction: column; align-items: center; gap: 14px;
  }
  .front-brand .brand-dot { width: 56px; height: 56px; }
  .front-brand .brand-name { font-size: 44px; }
  .slogan {
    position: absolute; left: 0; width: 238px; top: 256px; height: 36px;
    display: flex; align-items: center; justify-content: center;
    font-size: 14px; color: var(--ink);
  }
  .contact { position: absolute; left: 310px; top: 92px; color: var(--ink); }
  .contact .person { font-size: 18px; font-weight: 700; }
  .contact .role { font-size: 11px; color: var(--ink-soft); margin-top: 3px; }
  .contact ul { list-style: none; margin-top: 20px; }
  .contact li {
    display: flex; align-items: center; gap: 8px;
    font-size: 12px; height: 17px; margin-left: 0;
  }
  .contact li svg { width: 11px; height: 11px; flex: none; }
</style>
</head>
<body>
<div class="canvas">

  <section class="card card-back">
    <div class="photo-area" role="img" aria-label="Dark close-up photo of a phone with a cracked screen"></div>
    <div class="brand">
      <span class="brand-dot"></span>
      <span class="brand-name">dorvak</span>
    </div>
  </section>

  <section class="card card-front">
    <svg class="layout" width="482" height="292" viewBox="0 0 482 292">
      <rect width="482" height="292" fill="var(--paper)"/>
      <path d="M0 0 H238 C236 60 262 110 260 160 C258 205 248 232 238 256 H0 Z" fill="var(--panel)"/>
      <path d="M240 0 C238 60 264 110 262 160 C260 205 250 232 240 256" fill="none" stroke="var(--orange)" stroke-width="5"/>
      <polygon points="0,256 248,256 236,292 0,292" fill="var(--grey-band)"/>
      <polygon points="244,277 482,277 482,292 238,292" fill="var(--panel)"/>
    </svg>

    <div class="front-brand">
      <span class="brand-dot"></span>
      <span class="brand-name">dorvak</span>
    </div>

    <div class="slogan">Because Quality Matters</div>

    <div class="contact">
      <div class="person">Lars Vintorp</div>
      <div class="role">Managing Director</div>
      <ul>
        <li>
          <svg viewBox="0 0 12 12"><path d="M1 4 Q6 0 11 4 L9.5 5.5 L8 4.5 L8 3.5 Q6 3 4 3.5 L4 4.5 L2.5 5.5 Z M3 6 H9 L10 11 H2 Z" fill="var(--orange)"/></svg>
          0031612873406
        </li>
        <li>
          <svg viewBox="0 0 12 12"><circle cx="6" cy="6" r="5" fill="none" stroke="var(--orange)" stroke-width="1.4"/><ellipse cx="6" cy="6" rx="2" ry="5" fill="none" stroke="var(--orange)" stroke-width="1.2"/><line x1="1" y1="6" x2="11" y2="6" stroke="var(--orange)" stroke-width="1.2"/></svg>
          Lars@dorvak-example.nl
        </li>
        <li>
          <svg viewBox="0 0 12 12"><rect x="0.5" y="2" width="11" height="8" fill="var(--orange)"/><path d="M0.5 2 L6 6.5 L11.5 2" fill="none" stroke="var(--white)" stroke-width="1"/></svg>
          www.dorvak-example.nl
        </li>
      </ul>
    </div>
  </section>

</div>
</body>
</html>
```